VornaDerm/The experts in permanent hairremoval

Our Brand is VornaDerm and we are specialized on permantent hair removal for the body for men and woman. VornaDerm is working as a Franchise chain.
The brand should be positioned as lifestyle brand but with a medical background. People should trust in us. We take care about their body. This need to be communicated 100%.
Our system is inexpensive but we don't want to show that we are cheap. So we want to communicate that permanent hair removal is a real lifestyle product but affordable.
We already created a logo that you can see the style and colour we prefer.

Target Market(s)

Europe beginning (especially german spoken markets), Middle East, Africa

Industry/Entity Type

Hair Removal

Number of Pages Required

5+ page

Font styles to use
Serif
Other font styles liked:
• Trajan Pro

Requirements
Nice to have
• We are very open for new ideas

```html
<!DOCTYPE html>
<html lang="en">
<head>
<meta charset="utf-8">
<title>VornaDerm – Permanent Hair Removal</title>
<link href="https://fonts.googleapis.com/css2?family=Open+Sans:ital,wght@0,400;0,600;0,700;1,400;1,600&family=Roboto+Condensed:wght@400;700&family=Roboto:wght@300;400;500&display=swap" rel="stylesheet">
<style>
:root{
  --blue:#6eb0e2;
  --blue-nav:#72b2e2;
  --blue-btn:#5d9fd5;
  --blue-deep:#1d5b93;
  --ink:#333;
  --text:#555;
  --muted:#888;
  --grey-nav:#7a7a7a;
  --footer:#262626;
  --white:#fff;
  --star:#f0a818;
}
*{margin:0;padding:0;box-sizing:border-box}
html,body{width:1200px;height:2436px;overflow:hidden;background:var(--white)}
body{position:relative;font-family:"Open Sans",Arial,sans-serif;color:var(--text)}
.abs{position:absolute}

/* header */
.site-header{position:absolute;left:0;top:0;width:1200px;height:130px;background:#fcfcfc;border-bottom:1px solid #eee}
.brand{position:absolute;left:98px;top:38px;display:flex;align-items:center;gap:12px}
.brand-dot{width:40px;height:40px;border-radius:50%;background:var(--blue)}
.brand-name{font-family:"Open Sans",sans-serif;font-size:40px;font-weight:400;color:#7d7d7d;line-height:1}
.brand-tag{position:absolute;left:150px;top:86px;font-size:8px;color:#888;letter-spacing:.5px}
.lang-box{position:absolute;left:845px;top:48px;width:203px;height:42px;border:1px solid #ddd;border-radius:3px;display:flex;font-size:11px;color:#555;align-items:center}
.lang-box .lang{width:108px;height:100%;border-right:1px solid #ddd;display:flex;align-items:center;padding-left:14px;gap:8px;font-size:10px}
.flag{width:14px;height:9px;background:linear-gradient(#c33,#c33) 0 4px/14px 2px no-repeat,#2a4a8a}
.lang-box .price{flex:1;text-align:center;font-size:13px}
.cart{position:absolute;left:1061px;top:49px;width:40px;height:40px;border:2px solid var(--blue);border-radius:50%}
.cart-count{position:absolute;left:1083px;top:41px;width:16px;height:16px;border-radius:50%;background:var(--blue);color:#fff;font-size:9px;text-align:center;line-height:16px}

/* nav */
.main-nav{position:absolute;left:0;top:130px;width:1200px;height:52px;background:var(--blue-nav)}
.main-nav a{position:absolute;top:0;height:52px;line-height:52px;color:#fff;font-family:"Roboto",sans-serif;font-size:14px;text-decoration:none;letter-spacing:.3px}
.main-nav a.active{background:var(--grey-nav);width:81px;text-align:center}

/* hero */
.hero{position:absolute;left:0;top:182px;width:1200px;height:528px;background:linear-gradient(90deg,#e9eaee 0%,#dfe1e6 35%,#cfd2d8 60%,#e4e5e8 100%)}
.hero-title{position:absolute;left:110px;top:296px;font-family:"Roboto Condensed",sans-serif;font-weight:700;font-size:40px;line-height:46px;color:#3a3a3a}
.hero-title .accent{color:var(--blue-btn);font-size:48px}
.hero-text{position:absolute;left:110px;top:404px;font-size:13px;line-height:21px;color:#555}
.btn-book{position:absolute;left:110px;top:466px;width:221px;height:42px;background:var(--blue-btn);border:2px solid #9dc8ea;border-radius:3px;color:#fff;font-family:"Roboto",sans-serif;font-size:14px;text-align:center;line-height:38px}
.slide-arrow{position:absolute;top:440px;width:36px;height:36px;border-radius:50%;background:rgba(0,0,0,.08)}

/* why */
.section-title{position:absolute;left:0;width:1200px;text-align:center;font-family:"Roboto",sans-serif;font-weight:400;font-size:38px;color:#333}
.section-title span{color:var(--blue)}
.why-text{position:absolute;left:270px;top:829px;width:660px;text-align:center;font-size:11.5px;line-height:21px;color:#666}
.service{position:absolute;top:911px;width:260px;height:260px;border-radius:50%;border:6px solid #eee;box-shadow:0 0 0 1px #ddd;overflow:hidden}
.service .photo{position:absolute;inset:0}
.service .caption{position:absolute;left:0;bottom:0;width:100%;height:92px;background:rgba(40,40,40,.72);text-align:center;padding-top:14px;color:#fff}
.service .caption b{display:block;font-family:"Roboto",sans-serif;font-weight:500;font-size:14px}
.service .caption i{font-style:normal;font-size:12px}

/* testimonial */
.testimonial-bg{position:absolute;left:0;top:1221px}
.avatar{position:absolute;left:150px;top:1295px;width:170px;height:170px;border-radius:50%;border:5px solid #fff;background:linear-gradient(135deg,#e8d4c8,#c9a48e)}
.quote-badge{position:absolute;left:302px;top:1371px;width:36px;height:36px;border-radius:50%;background:#333;border:3px solid #fff;color:#fff;font-size:24px;font-weight:700;text-align:center;line-height:38px}
.testi-title{position:absolute;left:370px;top:1288px;font-family:"Roboto",sans-serif;font-style:italic;font-weight:300;font-size:32px;color:#fff}
.testi-quote{position:absolute;left:370px;top:1349px;width:690px;font-style:italic;font-size:13px;line-height:24px;color:#fff}
.testi-by{position:absolute;left:372px;top:1440px;font-size:15px;color:#fff}
.testi-dots{position:absolute;left:370px;top:1489px;display:flex;gap:3px}
.testi-dots span{width:34px;height:4px;background:#a8cff0}
.testi-dots span.on{background:#222}

/* welcome */
.welcome-title{position:absolute;left:99px;top:1622px;font-family:"Roboto",sans-serif;font-size:31px;color:#333}
.welcome-text{position:absolute;left:99px;width:600px;font-size:11.5px;line-height:21px;color:#555}
.ba-frame{position:absolute;left:745px;top:1629px;width:359px;height:206px;background:#fff;box-shadow:0 2px 8px rgba(0,0,0,.15)}
.ba-img{position:absolute;top:8px;width:164px;height:185px}
.ba-label{position:absolute;bottom:0;right:0;background:var(--blue);color:#fff;font-size:9px;font-weight:700;padding:4px 8px}
.ba-arrows{position:absolute;left:910px;top:1590px}

/* news */
.news-img{position:absolute;top:1903px;width:187px;height:164px}
.news-tag{position:absolute;top:0;right:0;background:var(--blue);color:#fff;font-size:11px;padding:6px 12px}
.news-body{position:absolute;top:1897px;width:260px}
.news-body h3{font-family:"Open Sans",sans-serif;font-weight:400;font-size:16px;color:#333;margin-bottom:10px}
.stars{color:var(--star);font-size:10px;letter-spacing:1px;margin-bottom:8px}
.stars .off{color:#ccc}
.news-body p{font-size:11.5px;line-height:21px;color:#555;margin-bottom:6px}
.news-body .more{font-size:12.5px;color:#333}

/* footer */
.site-footer{position:absolute;left:0;top:2121px;width:1200px;height:255px;background:var(--footer)}
.footer-brand{position:absolute;left:98px;top:2246px;display:flex;align-items:center;gap:10px;color:#fff;font-size:26px}
.footer-brand .brand-dot{width:30px;height:30px}
.footer-head{position:absolute;top:2160px;color:#fff;font-family:"Open Sans",sans-serif;font-weight:600;font-size:14.5px;letter-spacing:.3px}
.footer-text{position:absolute;color:#fff;font-size:11.5px;line-height:21px}
.field{position:absolute;left:346px;width:209px;height:43px;border:1px solid #ccc;color:#fff;font-size:11px;padding-left:14px;line-height:41px}
.subscribe{position:absolute;left:458px;top:2296px;width:97px;height:42px;background:var(--blue-deep);color:#fff;font-size:12.5px;text-align:center;line-height:42px}
.quick-links{position:absolute;left:664px;top:2198px;list-style:none}
.quick-links li{color:#fff;font-size:12px;line-height:24px}
.social{position:absolute;top:2318px;width:25px;height:25px;border:1px solid #ccc;border-radius:50%}
.bottom-bar{position:absolute;left:0;top:2376px;width:1200px;height:60px;background:var(--blue)}
.bottom-bar span{position:absolute;top:22px;color:#fff;font-size:11px}
</style>
</head>
<body>

<header class="site-header">
  <div class="brand"><div class="brand-dot"></div><div class="brand-name">VornaDerm</div></div>
  <div class="brand-tag">THE EXPERTS IN PERMANENT HAIR REMOVAL</div>
  <div class="lang-box"><div class="lang"><span class="flag"></span>ENGLISH ⌄</div><div class="price">$120.00</div></div>
  <div class="cart">
    <svg width="36" height="36" viewBox="0 0 36 36"><path d="M11 12h3l2 9h8l2-6H15" fill="none" stroke="#5d9fd5" stroke-width="2"/><circle cx="17" cy="24" r="1.5" fill="#5d9fd5"/><circle cx="23" cy="24" r="1.5" fill="#5d9fd5"/></svg>
  </div>
  <div class="cart-count">0</div>
</header>

<nav class="main-nav">
  <a class="active" style="left:98px">HOME</a>
  <a style="left:211px">ABOUT VORNADERM</a>
  <a style="left:387px">STUDIOS / PRICES</a>
  <a style="left:565px">FRANCHISE</a>
  <a style="left:696px">JOBS &amp; CAREERS</a>
  <a style="left:859px">ONLINE SHOP</a>
  <a style="left:1004px">CONTACT US</a>
</nav>

<section class="hero" role="img" aria-label="Photo of a woman in protective glasses receiving a laser hair removal treatment on the underarm"></section>
<h1 class="hero-title">PERMANENT<br><span class="accent">HAIR REMOVAL</span></h1>
<p class="hero-text">Lorem ipsum dolor sit amet, consectetur adipiscing elit,<br>sed do eiusmod tempor incididunt</p>
<div class="btn-book">BOOK YOUR APPOINTMENT</div>
<div class="slide-arrow" style="left:28px"></div>
<div class="slide-arrow" style="left:1134px"></div>

<h2 class="section-title" style="top:743px">Why <span>Permanent</span> Epilation</h2>
<svg class="abs" style="left:562px;top:799px" width="76" height="16" viewBox="0 0 76 16"><line x1="0" y1="8" x2="76" y2="8" stroke="#6eb0e2" stroke-width="1.5"/><circle cx="8" cy="8" r="5" fill="#fff" stroke="#6eb0e2" stroke-width="1.5"/><circle cx="38" cy="8" r="5" fill="#fff" stroke="#6eb0e2" stroke-width="1.5"/><circle cx="68" cy="8" r="5" fill="#fff" stroke="#6eb0e2" stroke-width="1.5"/></svg>
<p class="why-text">Nulla quis lorem ut libero malesuada feugiat. Curabitur non nulla sit amet nisl tempus convallis quis ac lectus. Quisque velit nisi, pretium ut lacinia in, elementum id enim. Nulla quis lorem ut libero malesuada feugiat. Curabitur</p>

<div class="service" style="left:164px"><div class="photo" role="img" aria-label="Photo of a laser hair removal treatment on a man" style="background:linear-gradient(135deg,#d9c2b0,#a8836a)"></div><div class="caption"><b>HAIR REMOVAL MEN</b><i>Nemo enim ipsam voluptate</i></div></div>
<div class="service" style="left:468px"><div class="photo" role="img" aria-label="Photo of a woman in goggles during a treatment" style="background:linear-gradient(135deg,#eceaf0,#c8c3cf)"></div><div class="caption"><b>HAIR REMOVAL MEN</b><i>Nemo enim ipsam voluptate</i></div></div>
<div class="service" style="left:771px"><div class="photo" role="img" aria-label="Photo of a hair removal device in use" style="background:linear-gradient(135deg,#e05070,#f2e8e8)"></div><div class="caption"><b>HAIR REMOVAL MEN</b><i>Nemo enim ipsam voluptate</i></div></div>

<svg class="testimonial-bg" width="1200" height="360" viewBox="0 0 1200 360"><path d="M0 0H1200V355C1060 300 900 300 760 318C560 344 300 370 0 318Z" fill="#6eb0e2"/></svg>
<div class="avatar" role="img" aria-label="Portrait photo of a client"></div>
<div class="quote-badge">“</div>
<h2 class="testi-title">What our clients say</h2>
<p class="testi-quote">“ Lorem ipsum dolor sit amet, consectetur adipiscing elit, sed do eiusmod tempor incididunt ut labore et dolore magna aliqua. Ut enim ad minim veniam, quis nostrud exercitation ullamco laboris nisi ut aliquip ex ea commodo consequat. Duis aute irure dolor in reprehenderit in voluptate velit esse cillum dolore eu fugiat nulla pariatur. ”</p>
<p class="testi-by">By Mara Lind</p>
<div class="testi-dots"><span class="on"></span><span></span><span></span></div>

<h2 class="welcome-title">WELCOME TO VORNADERM</h2>
<p class="welcome-text" style="top:1671px">Lorem ipsum dolor sit amet, consectetur adipiscing elit, sed do eiusmod tempor incididunt ut labore et dolore magna aliqua. Ut enim ad minim veniam, quis nostrud exercitation ullamco laboris nisi ut aliquip ex ea commodo consequat. Duis aute irure dolor in reprehenderit in voluptate velit esse cillum dolore eu fugiat nulla pariatur. Excepteur sint occaecat cupidatat non proident, sunt in culpa</p>
<p class="welcome-text" style="top:1765px">Lorem ipsum dolor sit amet, consectetur adipiscing elit, sed do eiusmod tempor incididunt ut labore et dolore magna aliqua. Ut enim ad minim veniam, quis nostrud exercitation ullamco laboris nisi ut aliquip ex ea commodo consequat. Duis aute irure dolor in reprehenderit in voluptate</p>

<svg class="ba-arrows" width="34" height="18" viewBox="0 0 34 18"><path d="M10 3L4 9l6 6M24 3l6 6-6 6" fill="none" stroke="#aaa" stroke-width="1.5"/></svg>
<div class="ba-frame">
  <div class="ba-img" role="img" aria-label="Before photo: underarm treatment" style="left:12px;background:linear-gradient(135deg,#f0f0f0,#d8d4d0)"><span class="ba-label">BEFORE</span></div>
  <div class="ba-img" role="img" aria-label="After photo: woman showing smooth underarm" style="left:184px;background:linear-gradient(135deg,#d8c0a8,#f2ede8)"><span class="ba-label">AFTER</span></div>
</div>

<div class="news-img" role="img" aria-label="Photo of a leg waxing treatment" style="left:99px;background:linear-gradient(135deg,#f3e6d8,#e0a870)"><span class="news-tag">NEWS</span></div>
<div class="news-body" style="left:310px"><h3>Nulla at diam ornare, aliquam urna</h3><div class="stars">★★★<span class="off">★★</span></div><p>Nulla at diam ornare, aliquam urna vel, commodo urna. Nam id risus a est luctus consectetur quis eget libero. Suspendisse potenti. Pellentesque habitant morbi tristique senectus</p><div class="more">Read More +</div></div>

<div class="news-img" role="img" aria-label="Photo of a laser treatment on a leg" style="left:630px;background:linear-gradient(135deg,#f4f2f0,#d6cfc8)"><span class="news-tag">NEWS</span></div>
<div class="news-body" style="left:841px"><h3>Nulla at diam ornare, aliquam urna</h3><div class="stars">★★★<span class="off">★★</span></div><p>Nulla at diam ornare, aliquam urna vel, commodo urna. Nam id risus a est luctus consectetur quis eget libero. Suspendisse potenti. Pellentesque habitant morbi tristique senectus</p><div class="more">Read More +</div></div>

<footer class="site-footer"></footer>
<div class="footer-brand"><div class="brand-dot"></div>VornaDerm</div>

<div class="footer-head" style="left:346px">SIGN UP TO RECEIVE EMAIL</div>
<p class="footer-text" style="left:346px;top:2192px;width:220px">Excepteur sint occaecat cupidatat non proident, sunt in culpa qui</p>
<div class="field" style="top:2244px">Enter Name</div>
<div class="field" style="top:2296px">Enter Email</div>
<div class="subscribe">SUBSCRIBE</div>

<div class="footer-head" style="left:664px">QUICK LINKS</div>
<ul class="quick-links"><li>About VornaDerm</li><li>Studios / Prices</li><li>Franchise</li><li>Jobs &amp; Careers</li><li>Online Shop</li><li>Contact Us</li></ul>

<div class="footer-head" style="left:879px">CONTACT US</div>
<p class="footer-text" style="left:879px;top:2194px">VornaDerm<br>P.O. BOX 210, LINDEN, GA 30999</p>
<svg class="abs" style="left:880px;top:2248px" width="18" height="18" viewBox="0 0 18 18"><path d="M4 2l3 3-2 2c1 2 3 4 5 5l2-2 3 3-2 2C8 15 3 10 2 4z" fill="none" stroke="#fff" stroke-width="1.3"/></svg>
<p class="footer-text" style="left:912px;top:2246px;font-size:13px">+1 555.014.2290</p>
<svg class="abs" style="left:880px;top:2275px" width="18" height="14" viewBox="0 0 18 14"><rect x="1" y="1" width="16" height="12" fill="none" stroke="#fff" stroke-width="1.3"/><path d="M1 1l8 7 8-7" fill="none" stroke="#fff" stroke-width="1.3"/></svg>
<p class="footer-text" style="left:912px;top:2271px;font-size:13px">info@vornaderm.com</p>
<div class="social" style="left:879px"></div>
<div class="social" style="left:909px"></div>
<div class="social" style="left:940px"></div>
<div class="social" style="left:971px"></div>

<div class="bottom-bar">
  <span style="left:99px">©2014 - 2015 VornaDerm, All Rights Reserved.</span>
  <span style="left:931px">Terms of Service | Privacy Policy</span>
</div>

</body>
</html>
```